Flyer-Design für Autolackiererei
Hallo es muss nur noch die Richtige Telefonnumer rein , die bekomm ich esrt von Fernolux zu geschickt
Zielgruppe
Karosserie & Autolackiererei
Autohäuser , Privatkunden , Bussunterhemen , LKW Unterhemen , Versicherungen
Aufgabenstellung
Neueröffung Von Autolackiererei ab 01.03.2019 bitte ganz wichtig muss auf flayer drauf.
Unfallinstansetztung , Fahrzeuglackierung Jeglicher Art , Oldtimer Restauration , Fahrzeugaufbereitung , Achsvermessung ,Felgen Lackieren ,Hagelschaden ,
inspektionen alle Fahrzeug Fabrikaten, Vexa, Reifenservice
Hol und Bring service ,scheibenaustausch abwicklung mit versicherung ,
Smart Repair

```html
<!DOCTYPE html>
<html lang="de">
<head>
<meta charset="utf-8">
<title>Flyer Autolackiererei Solwen</title>
<link rel="stylesheet" href="https://fonts.googleapis.com/css2?family=Signika:wght@400;600;700&display=swap">
<style>
  :root {
    --blue: #1a9fdb;
    --blue-light: #8fc8ec;
    --grey: #6d6c6e;
    --grey-dark: #58575a;
    --white: #ffffff;
    --canvas: #d9d9d9;
  }
  * { box-sizing: border-box; margin: 0; padding: 0; }
  html, body { width: 1200px; height: 932px; overflow: hidden; }
  body {
    background: var(--canvas);
    font-family: "Signika", sans-serif;
    position: relative;
  }
  .flyer {
    position: absolute;
    top: 110px;
    width: 340px;
    height: 679px;
    overflow: hidden;
  }
  .flyer--front { left: 235px; background: linear-gradient(160deg, #8e8d8f 0%, #c9c9ca 35%, #f2f2f2 60%, #b9b9ba 100%); }
  .flyer--back { left: 625px; background: var(--white); }

  .top-band {
    position: absolute; left: 0; top: 0; width: 100%; height: 33px;
    background: var(--blue); color: var(--white);
    font-weight: 600; font-size: 11.6px; letter-spacing: .6px;
    display: flex; align-items: center; justify-content: center;
  }
  .logo-tab {
    position: absolute; left: 55px; top: 33px; width: 229px; height: 227px;
    background: var(--white);
    border-radius: 0 0 115px 115px;
    display: flex; flex-direction: column; align-items: center; justify-content: center; gap: 10px;
  }
  .brand-dot { width: 70px; height: 70px; border-radius: 50%; background: var(--blue); }
  .brand-name { color: var(--grey); font-weight: 600; font-size: 16px; text-align: center; line-height: 1.2; }

  .partner-title {
    position: absolute; left: 26px; top: 279px;
    color: var(--blue); font-weight: 700; font-size: 17px; letter-spacing: .2px;
  }
  .bullets { list-style: none; position: absolute; }
  .bullets li { position: relative; padding-left: 7px; }
  .bullets li::before {
    content: ""; position: absolute; left: 0; top: .45em;
    border-left: 4px solid currentColor; border-top: 3px solid transparent; border-bottom: 3px solid transparent;
  }
  .bullets--front { left: 26px; top: 302px; color: var(--grey); font-size: 13px; line-height: 14.5px; font-weight: 600; }
  .bullets--front li { margin-bottom: 5.5px; }
  .bullets--front li::before { color: var(--blue); }

  .photo { position: absolute; left: 0; width: 100%; }
  .photo--front { top: 445px; height: 234px; background: linear-gradient(120deg, #b79a7a 0%, #7b8a99 40%, #2c4a6a 70%, #1f6fa8 100%); }
  .photo--back { top: 426px; height: 127px; background: linear-gradient(110deg, #dfe3e8 0%, #8a97a6 35%, #4b4f56 65%, #2b2b30 100%); }

  .badge {
    position: absolute; border-radius: 50%;
    display: flex; align-items: center; justify-content: center; text-align: center;
    color: var(--white); font-weight: 700; transform: rotate(-6deg);
  }
  .badge--grey { background: var(--grey); font-size: 10.3px; line-height: 12.5px; letter-spacing: .4px; }
  .badge--blue { background: var(--blue); }
  .front-open { left: 124px; top: 430px; width: 150px; height: 150px; font-size: 21px; line-height: 26px; letter-spacing: .8px; }
  .front-open .date { font-size: 16px; }
  .front-pickup { left: 236px; top: 394px; width: 88px; height: 88px; }
  .back-pickup { left: 234px; top: 309px; width: 90px; height: 90px; }
  .back-insurance { left: 155px; top: 365px; width: 122px; height: 122px; font-size: 14px; line-height: 17px; letter-spacing: .5px; }

  .contact-line {
    position: absolute; left: 0; width: 100%; top: 651px; text-align: center;
    color: var(--white); font-weight: 600; font-size: 11.3px; letter-spacing: .7px;
  }

  .back-top {
    position: absolute; left: 0; top: 0; width: 100%; height: 426px;
    background: linear-gradient(165deg, var(--blue) 0%, #3aa8e0 45%, var(--blue-light) 80%, #d6e9f6 100%);
  }
  .opening-tag {
    position: absolute; left: 32px; top: 28px; width: 192px; height: 19px;
    background: var(--grey); color: var(--white);
    font-weight: 600; font-size: 11px; letter-spacing: .8px;
    display: flex; align-items: center; padding-left: 2px;
  }
  .claim {
    position: absolute; left: 32px; top: 64px;
    color: var(--white); font-weight: 600; font-size: 16.5px; line-height: 19.5px;
  }
  .services-title {
    position: absolute; left: 32px; top: 144px;
    color: var(--white); font-weight: 700; font-size: 14.5px; letter-spacing: .5px;
  }
  .bullets--back { left: 32px; top: 164px; color: var(--white); font-size: 13.7px; line-height: 19.7px; font-weight: 600; }
  .bullets--back li::before { color: var(--grey); }

  .address {
    position: absolute; left: 32px; top: 573px;
    color: var(--grey-dark); font-weight: 600; font-size: 9.3px; line-height: 12.5px; letter-spacing: .6px;
  }
  .address p + p { margin-top: 10px; }
  .brand-small {
    position: absolute; left: 220px; top: 583px; width: 110px;
    display: flex; flex-direction: column; align-items: center; gap: 5px;
  }
  .brand-small .brand-dot { width: 40px; height: 40px; }
  .brand-small .brand-name { font-size: 10.5px; }
</style>
</head>
<body>

<section class="flyer flyer--front">
  <div class="top-band">ALLE FAHRZEUGE. ALLE FABRIKATE.</div>
  <div class="logo-tab">
    <span class="brand-dot"></span>
    <span class="brand-name">Autolackiererei<br>Solwen</span>
  </div>
  <h2 class="partner-title">IHR PARTNER FÜR IHR FAHRZEUG:</h2>
  <ul class="bullets bullets--front">
    <li>Fahrzeuglackierung und -<br>Aufbereitung jeglicher Art</li>
    <li>Inspektionen, Vexa und Reifenservice</li>
    <li>Hol- und Bringservice</li>
    <li>Scheibenreparatur und -tausch inkl.<br>Abwicklung mit Ihrer Versicherung</li>
  </ul>
  <div class="photo photo--front" role="img" aria-label="Foto: Hände mit Poliermaschine an einem blauen Auto"></div>
  <div class="badge badge--blue front-open"><span>NEU<br>ERÖFFNUNG<br><span class="date">01.03.2019</span></span></div>
  <div class="badge badge--grey front-pickup"><span>HOL- UND<br>BRINGSERVICE</span></div>
  <p class="contact-line">0251 / 48 31 72 09 | WWW.SOLWEN-LACK.DE</p>
</section>

<section class="flyer flyer--back">
  <div class="back-top"></div>
  <div class="opening-tag">NEUERÖFFNUNG AM 01.03.2019</div>
  <p class="claim">Farbe sprühen viele.<br>Wir versprühen Qualität für Ihr<br>Fahrzeug und echten Service für Sie!</p>
  <h2 class="services-title">UNSERE LEISTUNGEN:</h2>
  <ul class="bullets bullets--back">
    <li>Unfallinstansetztung</li>
    <li>Fahrzeuglackierungen jeglicher Art</li>
    <li>Oldtimer-Restauration</li>
    <li>Fahrzeugaufbereitung</li>
    <li>Achsvermessung</li>
    <li>Felgen Lackierung</li>
    <li>Beseitigung von Hagelschäden</li>
    <li>Inspektionen für alle Fabrikate</li>
    <li>Vexa</li>
    <li>Reifenservice</li>
    <li>Scheibenaustausch</li>
    <li>Smart Repair</li>
  </ul>
  <div class="photo photo--back" role="img" aria-label="Foto: Hand im Handschuh poliert einen Autoscheinwerfer"></div>
  <div class="badge badge--grey back-pickup"><span>HOL- UND<br>BRINGSERVICE</span></div>
  <div class="badge badge--blue back-insurance"><span>ABWICKLUNG<br>MIT IHRER<br>VERSICHERUNG</span></div>
  <div class="address">
    <p>LINDENWEG 14<br>48151 Halvering</p>
    <p>0251 / 48 31 72 09</p>
    <p>kontakt@solwen-lack.de<br>www.solwen-lack.de</p>
  </div>
  <div class="brand-small">
    <span class="brand-dot"></span>
    <span class="brand-name">Autolackiererei Solwen</span>
  </div>
</section>

</body>
</html>
```